BOLT Banner Ads for businesses who are keeping up with NRB guidelines

Banner ads - banner ad templates for us to advertise. We need this to be available in all of the key sizes for pomvia adlines and VS. Keep in mind, I want the template so we can adjust the wording. Sample wording is below:
NRB Compliant; BOLT Certified
Worried about COVID 19? Visit BOLT Certified Businesses
Protect you and your family, go to BOLT Certified Businesses
We are BOLT Certified, come see us today!
BOLT Certified businesses; giving you confidence
Be Confident with a BOLT Certification

Please feel free to check out our other contests for a better sense of the look and feel:
https://jobs.crewmosaic.com/job/5162078
https://jobs.crewmosaic.com/job/5162391

Target Market(s)

These ads are aimed at the general public to announce the certification.

Requirements
Must have
• We need the different banner sizes for pomvia adlines, vexaspot marketing, etc.

```html
<!DOCTYPE html>
<html lang="en">
<head>
<meta charset="utf-8">
<title>BOLT Certified – Visit Us Banner</title>
<link rel="stylesheet" href="https://fonts.googleapis.com/css2?family=Saira+Semi+Condensed:wght@400;700&family=Montserrat:wght@400;700&display=swap">
<style>
  :root {
    --navy: #002b55;
    --sky: #7bbde8;
    --ocean: #0a6ebd;
    --lime: #7ec44b;
    --white: #ffffff;
    --photo-light: #dfe9f1;
    --photo-dark: #1d2630;
  }
  * { margin: 0; padding: 0; box-sizing: border-box; }
  html, body { width: 1200px; height: 1200px; overflow: hidden; background: var(--white); }
  .banner { position: relative; width: 1200px; height: 1200px; overflow: hidden; background: var(--white); }
  .backdrop { position: absolute; inset: 0; }
  .brand {
    position: absolute; left: 72px; top: 110px;
    display: flex; align-items: center; gap: 22px;
    color: var(--navy);
    font-family: "Saira Semi Condensed", sans-serif; font-weight: 400;
  }
  .brand-dot { width: 120px; height: 120px; border-radius: 50%; background: var(--ocean); }
  .brand-name { line-height: 1; }
  .brand-name .word { display: block; font-size: 112px; letter-spacing: 2px; }
  .brand-name .sub { display: block; font-size: 30px; letter-spacing: 8px; margin-top: 2px; }
  .headline {
    position: absolute; left: 84px; top: 466px;
    font-family: "Saira Semi Condensed", sans-serif; font-weight: 700;
    font-size: 70px; line-height: 90px; color: var(--white); text-transform: uppercase;
  }
  .headline .accent { color: var(--lime); }
  .headline .quote-close { color: var(--white); }
  .subline {
    position: absolute; left: 84px; top: 772px;
    font-family: "Saira Semi Condensed", sans-serif; font-weight: 700;
    font-size: 54px; line-height: 72px; color: var(--white); text-transform: uppercase;
  }
  .cta {
    position: absolute; left: 590px; top: 754px; width: 378px; height: 378px;
    border-radius: 50%; background: var(--lime);
    display: flex; flex-direction: column; align-items: center; justify-content: center;
    font-family: "Saira Semi Condensed", sans-serif; font-weight: 700;
    font-size: 100px; line-height: 108px; color: var(--white);
  }
  .contact { position: absolute; left: 78px; top: 1008px; display: flex; align-items: center; gap: 24px; }
  .contact-icon { width: 70px; height: 86px; }
  .contact-text { font-family: "Montserrat", sans-serif; color: var(--white); }
  .contact-label { font-size: 26px; font-weight: 400; line-height: 36px; }
  .contact-number { font-size: 42px; font-weight: 700; line-height: 54px; letter-spacing: 1px; }
</style>
</head>
<body>
<div class="banner">
  <svg class="backdrop" width="1200" height="1200" viewBox="0 0 1200 1200">
    <defs>
      <linearGradient id="teamPhotoTone" x1="0" y1="0" x2="0" y2="1">
        <stop offset="0" stop-color="var(--photo-light)"/>
        <stop offset="0.45" stop-color="#c9d3dc"/>
        <stop offset="0.7" stop-color="#3a434d"/>
        <stop offset="1" stop-color="var(--photo-dark)"/>
      </linearGradient>
    </defs>
    <circle class="sky-disc" cx="969" cy="-186" r="413" fill="var(--sky)"/>
    <circle class="ocean-ring" cx="1010" cy="600" r="470" fill="var(--ocean)"/>
    <circle class="photo-frame" cx="987" cy="553" r="462" fill="var(--white)"/>
    <circle class="team-photo" cx="987" cy="553" r="447" fill="url(#teamPhotoTone)"
            role="img" aria-label="Photo of three smiling business professionals in suits"/>
    <circle class="navy-field" cx="75" cy="1110" r="812" fill="var(--navy)"
            stroke="var(--white)" stroke-width="14"/>
    <rect class="navy-edge-fix" x="0" y="1110" width="60" height="90" fill="var(--navy)"/>
  </svg>

  <div class="brand">
    <div class="brand-dot"></div>
    <div class="brand-name">
      <span class="word">BOLT</span>
      <span class="sub">Certification</span>
    </div>
  </div>

  <h1 class="headline">
    “We are<br>
    <span class="accent">BOLT</span><br>
    <span class="accent">Certified</span><span class="quote-close">”</span>
  </h1>

  <p class="subline">Come see us<br>today!</p>

  <div class="cta"><span>VISIT</span><span>US</span></div>

  <div class="contact">
    <svg class="contact-icon" viewBox="0 0 70 86" aria-hidden="true">
      <rect x="0" y="0" width="62" height="76" rx="6" fill="var(--lime)"/>
      <rect x="0" y="76" width="62" height="10" rx="4" fill="var(--lime)"/>
      <line x1="0" y1="74" x2="62" y2="74" stroke="var(--navy)" stroke-width="3"/>
      <rect x="65" y="8" width="5" height="14" rx="2" fill="var(--lime)"/>
      <rect x="65" y="30" width="5" height="14" rx="2" fill="var(--lime)"/>
      <rect x="65" y="52" width="5" height="14" rx="2" fill="var(--lime)"/>
      <path d="M17 22 c-4 4 -3 12 5 21 c8 9 17 12 22 8 l3 -3 c1 -1 1 -3 0 -4 l-6 -5 c-1 -1 -3 -1 -4 0 l-2 2 c-4 -2 -8 -6 -10 -10 l2 -2 c1 -1 1 -3 0 -4 l-5 -6 c-1 -1 -3 -1 -4 0 z"
            fill="none" stroke="var(--navy)" stroke-width="3.5" stroke-linejoin="round"/>
    </svg>
    <div class="contact-text">
      <p class="contact-label">More information call us</p>
      <p class="contact-number">000 555 214 680</p>
    </div>
  </div>
</div>
</body>
</html>
```